Electric mountain bike tours nz

We are an Electric Mountain bike tour company in New Zealand. We will be offering bike rental and guided tours around the Nelson region in New Zealand. I want our website to represent both Mountain biking and New Zealand with the colours layout and features. We want tabs for the following:
-1 about us
-2 what we offer
-3 bookings/contact
Under the about us tab will be who we are as a a company. I want the ability to add videos to each of these tabs as we move foward with videos of the tracks we will be riding. I want the website to be editable so I can add and remove videos/photos myself. Also "our bikes" will be under this tab.
Under the what we offer tab will be
-1 bike rental and pricing
-2 guided tours and pricing
-3 recommended package deals.
I want to able to put the tracks under the guided tours tab and select beginner/ intermediate/advanced and have the tracks in each of the following to match the rider level. Also to be able to have a small video of the track would be great in this section.
Bookings and contact tab
(Further information for this tab to be updated soon)
- Silver ferns, kiwi, mountains

```html
<!DOCTYPE html>
<html lang="en">
<head>
<meta charset="utf-8">
<title>TRAILVOLT – Electric Mountain Bike Tours</title>
<link href="https://fonts.googleapis.com/css2?family=Lato:wght@300;400;700;900&display=swap" rel="stylesheet">
<style>
:root{
  --green:#7cc242;
  --green-band:#5cb820;
  --green-dark:#2e6b12;
  --ink:#111111;
  --text:#333333;
  --muted:#9a9a9a;
  --grey-band:#e2e2e0;
  --footer:#050505;
  --footer-bar:#3a3a3a;
  --white:#ffffff;
}
*{box-sizing:border-box;margin:0;padding:0}
html,body{width:1200px;height:4157px;overflow:hidden}
body{font-family:'Lato',sans-serif;color:var(--text);background:var(--white);position:relative}
section,header,footer{position:absolute;left:0;width:1200px}
.abs{position:absolute}
.section-title{position:absolute;left:0;width:100%;text-align:center;font-size:29px;font-weight:700;color:var(--ink)}
.section-title span{color:var(--green);font-weight:400}
.section-title.light{color:var(--white)}
.body-copy{position:absolute;text-align:center;font-size:14.5px;line-height:1.6}
.read-more{position:absolute;display:flex;align-items:center;justify-content:space-between;width:116px;height:30px;background:var(--ink);color:var(--white);border-radius:15px;font-size:12px;font-weight:700;padding:0 5px 0 16px}
.read-more i{display:block;width:21px;height:21px;border-radius:50%;background:var(--white);position:relative}
.read-more i::after{content:"";position:absolute;left:6px;top:6px;border-left:8px solid var(--ink);border-top:5px solid transparent;border-bottom:5px solid transparent}
.photo{position:absolute}

/* header */
.site-header{top:0;height:140px;background:var(--white)}
.brand{left:70px;top:46px;display:flex;align-items:center;gap:10px;font-size:26px;font-weight:900;color:var(--ink)}
.brand-dot{width:40px;height:40px;border-radius:50%;background:var(--ink)}
.phone{left:862px;top:40px;font-size:17px;color:var(--ink);display:flex;align-items:center;gap:8px}
.socials{display:flex;gap:5px}
.socials b{display:block;width:18px;height:18px;background:var(--ink)}
.header-social{left:1028px;top:41px}
.main-nav{right:48px;top:82px;display:flex;gap:52px;font-size:15px;font-weight:700;color:var(--ink)}
.main-nav .active{color:var(--muted);font-weight:400}

/* hero */
.hero{top:140px;height:572px}
.hero .photo{inset:0;background:linear-gradient(160deg,#5b6f7d 0%,#8a9aa0 30%,#4b5a52 55%,#3b2a1e 80%,#21170f 100%)}
.hero-title{top:300px;left:0;width:100%;text-align:center;font-size:58px;font-weight:900;letter-spacing:3px;color:var(--white)}
.hero-sub{top:378px;left:0;width:100%;text-align:center;font-size:17px;line-height:1.45;color:var(--white)}
.slider-arrow{position:absolute;width:22px;height:22px;border-left:4px solid rgba(255,255,255,.85);border-bottom:4px solid rgba(255,255,255,.85)}
.slider-arrow.prev{transform:rotate(45deg)}
.slider-arrow.next{transform:rotate(-135deg)}

/* about */
.about{top:712px;height:673px}
.about-photo{top:128px;height:171px;background:linear-gradient(135deg,#5a6b3c,#8a7a5a 55%,#3e4a2e)}
.about-photo.first{border:7px solid var(--ink);background:linear-gradient(135deg,#4f7a2c,#a49a6a 55%,#3b5a22)}

/* our bike */
.our-bike{top:1385px;height:390px;background:var(--grey-band)}
.bike-badge{position:absolute;left:505px;top:-72px;width:190px;height:190px;border-radius:50%;background:var(--ink);border:10px solid var(--white)}

/* offer */
.offer{top:1782px;height:718px}
.offer > .photo{inset:0;background:linear-gradient(180deg,#3a4754 0%,#24313b 45%,#1b2329 100%)}
.card{position:absolute;width:286px;height:408px;background:var(--white)}
.card .photo{left:7px;top:7px;width:272px;height:232px}
.card h3{position:absolute;top:257px;left:0;width:100%;text-align:center;font-size:16px;font-weight:700;color:var(--ink)}
.card p{position:absolute;top:288px;left:28px;width:230px;text-align:center;font-size:12.5px;line-height:1.35;color:#444}
.card .read-more{left:85px;bottom:-14px}
.card .date{position:absolute;top:280px;left:0;width:100%;text-align:center;font-size:12.5px;color:#444}
.card .date + p{top:310px}
.img-lake{background:linear-gradient(180deg,#6e8cb0,#c8d5e3 40%,#4d6b55 70%,#2c3a28)}
.img-riders{background:linear-gradient(160deg,#b8c0b0,#7b8a70 40%,#3f3a30)}
.img-forest{background:linear-gradient(170deg,#9fc46a,#4d7a2c 50%,#2b4018)}

/* testimonial & video */
.social-proof{top:2500px;height:487px}
.split-title{position:absolute;top:68px;font-size:27px;font-weight:700;color:var(--ink)}
.split-title span{color:var(--muted);font-weight:400}
.divider{left:600px;top:58px;width:1px;height:300px;background:#dcdcdc}
.quote-box{left:130px;top:150px;width:394px;height:240px;border:2px solid #c9c9c9;border-radius:10px;background:var(--white)}
.quote-box p{position:absolute;left:60px;top:48px;width:310px;font-size:12.5px;line-height:1.35;color:#444}
.quote-mark{left:22px;top:44px;font-size:38px;font-weight:900;color:var(--ink);line-height:1}
.quote-tail{left:330px;top:230px;width:18px;height:18px;background:var(--white);border-right:2px solid #c9c9c9;border-bottom:2px solid #c9c9c9;transform:rotate(45deg)}
.avatar{left:150px;top:100px;width:92px;height:92px;border-radius:50%;background:linear-gradient(160deg,#d8dde3,#a7b2be);border:4px solid var(--white)}
.quote-name{left:438px;top:410px;font-size:14px;font-style:italic;color:var(--ink)}
.video{left:673px;top:138px;width:397px;height:240px;background:linear-gradient(150deg,#dfe8f0,#7d93ab 35%,#2a3a52 70%,#1a2230)}
.play{left:178px;top:88px;width:42px;height:42px;border-radius:50%;background:rgba(255,255,255,.9)}
.play::after{content:"";position:absolute;left:16px;top:12px;border-left:14px solid var(--ink);border-top:9px solid transparent;border-bottom:9px solid transparent}
.video-bar{left:0;bottom:0;width:100%;height:26px;background:#111}
.video-bar .track{position:absolute;left:64px;top:11px;width:316px;height:4px;background:#666}
.video-bar .track i{display:block;width:34%;height:100%;background:#d51f1f}
.ctrl{position:absolute;top:7px;left:12px;width:10px;height:12px;border-left:3px solid #fff;border-right:3px solid #fff}

/* blog */
.blog{top:2987px;height:643px}
.blog > .photo{inset:0;background:linear-gradient(180deg,#2f4a22 0%,#6a8c44 40%,#3d5a24 75%,#1f2e14 100%)}

/* newsletter */
.newsletter{top:3630px;height:75px;background:var(--green-band)}
.nl-icon{left:200px;top:20px;width:36px;height:36px;border-radius:50%;background:var(--white)}
.nl-icon svg{position:absolute;left:9px;top:11px}
.nl-title{left:252px;top:21px;font-size:25px;color:var(--white)}
.nl-arrow{left:482px;top:25px;width:18px;height:18px;border-right:3px solid var(--white);border-top:3px solid var(--white);transform:rotate(45deg)}
.nl-input{left:535px;top:22px;width:399px;height:30px;background:var(--white);font-size:11px;color:#777;padding:9px 12px}
.nl-button{left:945px;top:22px;width:130px;height:30px;background:var(--green-dark);color:var(--white);font-size:12px;font-weight:700;text-align:center;line-height:30px;letter-spacing:1px}

/* footer */
.site-footer{top:3705px;height:396px;background:var(--footer);color:var(--white)}
.footer-mark{right:30px;top:150px;font-size:120px;font-weight:900;color:rgba(255,255,255,.05)}
.footer-title{position:absolute;font-size:17px;font-weight:700}
.field{position:absolute;height:34px;border:1px solid #777;font-size:12px;padding:9px 10px;color:#ddd}
.submit{left:130px;top:314px;width:120px;height:28px;background:#a8a8a8;color:var(--white);font-size:13px;text-align:center;line-height:28px}
.contact-list{left:657px;top:118px;font-size:12.5px;line-height:1.55;color:#ddd;list-style:none}
.contact-list li{display:flex;align-items:center;gap:8px}
.contact-list .ico{width:9px;height:9px;border-radius:50%;background:#ddd;flex:none}
.quick-links{left:880px;top:118px;list-style:none;font-size:12.5px;line-height:1.7;color:#ddd}
.quick-links li::before{content:"›";margin-right:10px}
.footer-rule{position:absolute;height:1px;background:#444}
.footer-social .socials b{background:var(--white);width:19px;height:19px}
.call-number{left:880px;top:315px;font-size:29px;color:var(--white)}
.footer-bar{position:absolute;left:0;top:4101px;width:1200px;height:56px;background:var(--footer-bar);color:#ccc;font-size:13px;text-align:center;line-height:56px}
</style>
</head>
<body>

<header class="site-header">
  <div class="brand abs"><span class="brand-dot"></span>TRAILVOLT</div>
  <div class="phone abs">
    <svg width="14" height="14" viewBox="0 0 24 24"><path d="M6.6 10.8a15.1 15.1 0 0 0 6.6 6.6l2.2-2.2c.3-.3.7-.4 1-.2 1.1.4 2.3.6 3.6.6.6 0 1 .4 1 1V20c0 .6-.4 1-1 1A17 17 0 0 1 3 4c0-.6.4-1 1-1h3.5c.6 0 1 .4 1 1 0 1.3.2 2.5.6 3.6.1.3 0 .7-.2 1z" fill="#111"/></svg>
    (555) 014 2290
  </div>
  <div class="socials header-social abs"><b></b><b></b><b></b><b></b></div>
  <nav class="main-nav abs">
    <span class="active">About us</span><span>What we offer</span><span>Bookings/Contact</span>
  </nav>
</header>

<section class="hero">
  <div class="photo" role="img" aria-label="Mountain biker riding a rocky ridge above a valley at dusk"></div>
  <span class="slider-arrow prev" style="left:66px;top:418px"></span>
  <span class="slider-arrow next" style="left:1112px;top:418px"></span>
  <h1 class="hero-title abs">TRAILVOLT</h1>
  <p class="hero-sub abs">We are an Electric Mountain bike tour company in New Zealand.<br>We will be offering bike rental and guided tours around the Nelson region in New Zealand.</p>
</section>

<section class="about">
  <h2 class="section-title" style="top:54px">About <span>Us</span></h2>
  <div class="photo about-photo first" style="left:152px;width:278px" role="img" aria-label="Riders on a forest trail"></div>
  <div class="photo about-photo" style="left:457px;width:286px" role="img" aria-label="Mountain biker on a dirt path"></div>
  <div class="photo about-photo" style="left:762px;width:283px" role="img" aria-label="Riders crossing a wooded track"></div>
  <p class="body-copy" style="left:120px;top:322px;width:960px">Lorem ipsum dolor sit amet, consectetuer adipiscing elit. Aenean commodo ligula eget dolor. Aenean massa. Cum sociis natoque penatibus et magnis dis parturient montes, nascetur ridiculus mus. Donec quam felis, ultricies nec, pellentesque eu, pretium quis, sem. Nulla consequat massa quis enim. Donec pede justo, fringilla vel, aliquet nec, vulputate eget, arcu.In enim justo, rhoncus ut, imperdiet a, venenatis vitae, justo. Nullam dictum felis eu pede mollis pretium.Integer tincidunt. Cras dapibus. Vivamus elementum semper nisi.</p>
  <div class="read-more" style="left:542px;top:481px">Read More<i></i></div>
</section>

<section class="our-bike">
  <div class="bike-badge" role="img" aria-label="Gear-ring badge with a mountain bike icon"></div>
  <h2 class="section-title" style="top:155px;font-size:27px">Our Bike</h2>
  <p class="body-copy" style="left:130px;top:205px;width:940px">Lorem ipsum dolor sit amet, consectetuer adipiscing elit. Aenean commodo ligula eget dolor. Aenean massa. Cum sociis natoque penatibus et magnis dis parturient montes, nascetur ridiculus mus. Donec quam felis, ultricies nec, pellentesque eu</p>
  <div class="read-more" style="left:542px;top:290px">Read More<i></i></div>
</section>

<section class="offer">
  <div class="photo" role="img" aria-label="Misty mountain landscape at dusk"></div>
  <h2 class="section-title light" style="top:56px;font-size:27px">What we <span>Offer</span></h2>
  <p class="body-copy" style="left:230px;top:115px;width:740px;color:#fff">Lorem ipsum dolor sit amet, consectetuer adipiscing elit. Aenean commodo ligula eget dolor. Aenean massa. Cum sociis natoque penatibus et magnis dis parturient montes, nascetur ridiculus mus.</p>
  <span class="slider-arrow prev" style="left:60px;top:403px"></span>
  <span class="slider-arrow next" style="left:1118px;top:403px"></span>
  <article class="card" style="left:139px;top:221px">
    <div class="photo img-lake" role="img" aria-label="Electric mountain bike parked above a lake"></div>
    <h3>Bike rental &amp; pricing</h3>
    <p>Lorem ipsum dolor sit amet, consectetuer adipiscing elit. Aenean commodo ligula eget dolor. Aenean massa. Cum sociis natoque penatibus et magnis dis parturient montes, nascetur ridiculus mus.</p>
    <div class="read-more">Read More<i></i></div>
  </article>
  <article class="card" style="left:454px;top:221px">
    <div class="photo img-riders" role="img" aria-label="Two riders standing with fat-tyre bikes"></div>
    <h3>Guided tours &amp; pricing</h3>
    <p>Lorem ipsum dolor sit amet, consectetuer adipiscing elit. Aenean commodo ligula eget dolor. Aenean massa. Cum sociis natoque penatibus et magnis dis parturient montes, nascetur ridiculus mus.</p>
    <div class="read-more">Read More<i></i></div>
  </article>
  <article class="card" style="left:768px;top:221px">
    <div class="photo img-forest" role="img" aria-label="Riders on a green forest trail"></div>
    <h3>Recommended package deals</h3>
    <p>Lorem ipsum dolor sit amet, consectetuer adipiscing elit. Aenean commodo ligula eget dolor. Aenean massa. Cum sociis natoque penatibus et magnis dis parturient montes, nascetur ridiculus mus.</p>
    <div class="read-more">Read More<i></i></div>
  </article>
</section>

<section class="social-proof">
  <h2 class="split-title" style="left:282px">Client <span>Testimonials</span></h2>
  <h2 class="split-title" style="left:673px">Featured <span>Vedeo</span></h2>
  <div class="divider abs"></div>
  <div class="quote-box abs">
    <span class="quote-mark abs">“</span>
    <p>Lorem ipsum dolor sit amet, consectetuer adipiscing elit. Quid autem habent admirationis, cum prope accesseris? At hoc quaque, alter in vita? Non igit ur de improbo, sed de callido improbo quaerimus, qualis Duo Reges: constructio interrete. Quae hic rei publicae vel conscientia? Quis hoc non vidit? Ut pro me ipsa virtus nec dubitabit tell vestro beate M. Nihil ad rem! Ne sit sane; Nihil ad rem! Ne sit sane.</p>
    <span class="quote-tail abs"></span>
  </div>
  <div class="avatar abs" role="img" aria-label="Client portrait"></div>
  <span class="quote-name abs">Harper.R.L.</span>
  <div class="video abs" role="img" aria-label="Video still of a rider on a snowy trail">
    <span class="play abs"></span>
    <div class="video-bar abs"><span class="ctrl"></span><span class="track"><i></i></span></div>
  </div>
</section>

<section class="blog">
  <div class="photo" role="img" aria-label="Sunlit forest with tall trees"></div>
  <h2 class="section-title light" style="top:52px;font-size:27px">Latest Blog</h2>
  <span class="slider-arrow prev" style="left:60px;top:326px"></span>
  <span class="slider-arrow next" style="left:1118px;top:326px"></span>
  <article class="card" style="left:139px;top:144px">
    <div class="photo img-lake" role="img" aria-label="Electric mountain bike parked above a lake"></div>
    <h3>Lorem ipsum dolor sit amet</h3>
    <span class="date">October 25, 2017.</span>
    <p>Lorem ipsum dolor sit amet, consectetuer adipiscing elit. Aenean commodo ligula eget dolor. Aenean massa.</p>
    <div class="read-more">Read More<i></i></div>
  </article>
  <article class="card" style="left:454px;top:144px">
    <div class="photo img-riders" role="img" aria-label="Two riders standing with fat-tyre bikes"></div>
    <h3>Lorem ipsum dolor sit amet</h3>
    <span class="date">October 25, 2017.</span>
    <p>Lorem ipsum dolor sit amet, consectetuer adipiscing elit. Aenean commodo ligula eget dolor. Aenean massa.</p>
    <div class="read-more">Read More<i></i></div>
  </article>
  <article class="card" style="left:768px;top:144px">
    <div class="photo img-forest" role="img" aria-label="Riders on a green forest trail"></div>
    <h3>Lorem ipsum dolor sit amet</h3>
    <span class="date">October 25, 2017.</span>
    <p>Lorem ipsum dolor sit amet, consectetuer adipiscing elit. Aenean commodo ligula eget dolor. Aenean massa.</p>
    <div class="read-more">Read More<i></i></div>
  </article>
</section>

<section class="newsletter">
  <span class="nl-icon abs"><svg width="18" height="13" viewBox="0 0 18 13"><rect x="0.5" y="0.5" width="17" height="12" fill="none" stroke="#5cb820" stroke-width="1.5"/><path d="M1 1l8 6 8-6" fill="none" stroke="#5cb820" stroke-width="1.5"/></svg></span>
  <span class="nl-title abs">News letter Signup</span>
  <span class="nl-arrow abs"></span>
  <div class="nl-input abs">Enter Your Email</div>
  <div class="nl-button abs">SUBSCRIBE</div>
</section>

<footer class="site-footer">
  <span class="footer-mark abs">TRAILVOLT</span>
  <h3 class="footer-title" style="left:130px;top:62px">Booking</h3>
  <div class="field" style="left:130px;top:112px;width:214px">First Name:</div>
  <div class="field" style="left:355px;top:112px;width:213px">LastName :</div>
  <div class="field" style="left:130px;top:154px;width:214px">Phone No :</div>
  <div class="field" style="left:355px;top:154px;width:213px">Email Address :</div>
  <div class="field" style="left:130px;top:196px;width:438px;height:92px">Message :</div>
  <div class="submit abs">Submit</div>

  <h3 class="footer-title" style="left:657px;top:62px">Contact</h3>
  <div class="footer-rule" style="left:657px;top:98px;width:170px"></div>
  <ul class="contact-list abs">
    <li>42 Ridgeway Lane<br>Fernhill 7010</li>
    <li style="margin-top:6px"><span class="ico"></span>555-014-2290</li>
    <li><span class="ico"></span>hello@trailvolt.example</li>
    <li><span class="ico"></span>www.trailvolt.example</li>
  </ul>
  <h3 class="footer-title" style="left:657px;top:268px;font-size:15px;letter-spacing:1px">FOLLOW US ON</h3>
  <div class="footer-rule" style="left:657px;top:298px;width:170px"></div>
  <div class="footer-social abs" style="left:657px;top:314px"><div class="socials"><b></b><b></b><b></b><b></b></div></div>

  <h3 class="footer-title" style="left:880px;top:62px">Quick Links</h3>
  <div class="footer-rule" style="left:880px;top:98px;width:190px"></div>
  <ul class="quick-links abs">
    <li>About us</li><li>What we offer</li><li>Bookings/Contact</li>
  </ul>
  <h3 class="footer-title" style="left:880px;top:268px;font-size:15px;letter-spacing:1px">CALL US ON</h3>
  <div class="footer-rule" style="left:880px;top:298px;width:190px"></div>
  <span class="call-number abs">(555) 014 2290</span>
</footer>
<div class="footer-bar">© 2017 trailvolt &nbsp;|&nbsp; Privacy Policy &nbsp;|&nbsp; User Agreement</div>

</body>
</html>
```